Dorian Blakely & Morning Lanterns

I need a cd cover designed for a Gospel/Christian Choir. I'm attaching the main picture I want on the cover. This is our single "Lift my heart higher".

Requirements
Must have
• Single name: Lift My Heart Higher

```html
<!DOCTYPE html>
<html lang="en">
<head>
<meta charset="utf-8">
<title>Dorian Blakely &amp; Morning Lanterns — Lift My Heart Higher</title>
<link rel="stylesheet" href="https://fonts.googleapis.com/css2?family=Crimson+Text:wght@600;700&display=swap">
<style>
  :root {
    --night: #050403;
    --brick-glow: #8a3a12;
    --brick-deep: #2a120a;
    --lamp: #ffd36a;
    --ink-white: #ffffff;
    --gold: #f5b400;
    --shadow: rgba(0,0,0,0.85);
  }
  html, body {
    margin: 0;
    padding: 0;
    width: 1200px;
    height: 1200px;
    overflow: hidden;
    background: var(--night);
  }
  .cover {
    position: relative;
    width: 1200px;
    height: 1200px;
    overflow: hidden;
    background: var(--night);
    font-family: "Crimson Text", Georgia, serif;
  }
  .cover-photo {
    position: absolute;
    inset: 0;
  }
  .genre-line {
    position: absolute;
    top: 28px;
    left: 46px;
    right: 30px;
    margin: 0;
    color: var(--ink-white);
    font-size: 41px;
    font-weight: 600;
    letter-spacing: 0.38em;
    white-space: nowrap;
  }
  .title-block {
    position: absolute;
    right: 36px;
    bottom: 22px;
    text-align: right;
  }
  .artist {
    margin: 0;
    color: var(--ink-white);
    font-size: 98px;
    font-weight: 700;
    line-height: 0.92;
    letter-spacing: 0.01em;
    text-shadow: 4px 4px 6px var(--shadow), 0 0 14px var(--shadow);
  }
  .single-title {
    margin: 2px 0 0;
    color: var(--gold);
    font-size: 66px;
    font-weight: 700;
    line-height: 1;
    text-shadow: 3px 3px 5px var(--shadow);
  }
</style>
</head>
<body>
<main class="cover">
  <svg class="cover-photo" width="1200" height="1200" viewBox="0 0 1200 1200"
       role="img" aria-label="Photo of the choir leader in a dark satin suit leaning beside a lit brick wall under a street lamp at night">
    <defs>
      <linearGradient id="scene-tone" x1="0" y1="0" x2="1" y2="0">
        <stop offset="0" stop-color="#050403"/>
        <stop offset="0.35" stop-color="#120a06"/>
        <stop offset="0.6" stop-color="#3a1a0c"/>
        <stop offset="0.85" stop-color="#8a3a12"/>
        <stop offset="1" stop-color="#5a2a14"/>
      </linearGradient>
      <radialGradient id="lamp-glow" cx="420" cy="110" r="200" gradientUnits="userSpaceOnUse">
        <stop offset="0" stop-color="#ffe89a" stop-opacity="0.95"/>
        <stop offset="0.35" stop-color="#ff9a2a" stop-opacity="0.55"/>
        <stop offset="1" stop-color="#ff7a10" stop-opacity="0"/>
      </radialGradient>
      <linearGradient id="figure-tone" x1="0" y1="0" x2="0" y2="1">
        <stop offset="0" stop-color="#1c1a22" stop-opacity="0.0"/>
        <stop offset="0.3" stop-color="#1c1c28" stop-opacity="0.8"/>
        <stop offset="1" stop-color="#0c0c12" stop-opacity="0.95"/>
      </linearGradient>
    </defs>
    <rect width="1200" height="1200" fill="url(#scene-tone)"/>
    <rect width="1200" height="1200" fill="url(#lamp-glow)"/>
    <rect x="560" y="380" width="560" height="820" rx="200" fill="url(#figure-tone)"/>
  </svg>

  <p class="genre-line">Gospel &amp; Christian Choir</p>

  <div class="title-block">
    <h1 class="artist">Dorian Blakely &amp;<br>Morning Lanterns</h1>
    <h2 class="single-title">Lift My Heart Higher</h2>
  </div>
</main>
</body>
</html>
```